Album Cover Design – TAVREN “Sable Hours”

Hello, we are Corvane Records, representing artist TAVREN, who will release his second album on October 24, 2025. We are looking for a high-quality, artistic album cover design that will represent this new era of his music.
About the album:
Sable Hours represents a darker, bolder alter ego of TAVREN. It’s powerful, emotional, and mysterious - a step into a new world. The visuals should reflect this alter ego and dark chic mood of this era.
The first single, “KORAL,” is already released and sets the tone: vibrant but with an edge, bold and energetic.

Style we are looking for:
• Dark, bold, mysterious, yet elegant and premium
• Visually striking and memorable
• Modern and international feel

Additional guidance for designers:
Please research TAVREN to understand his style and artistic direction:
• YouTube: https://www.vidstreamhub.example/channel/QX7pLmR3vTnWcHsYdKeAbGfZ
• Website: www.tavren-music.example
Think of an iconic, timeless cover that captures both the darkness and the charisma of TAVREN.

Deliverables:
• Final album cover design (digital + print)
• Source files

```html
<!DOCTYPE html>
<html lang="en">
<head>
<meta charset="utf-8">
<title>TAVREN — Sable Hours</title>
<link rel="stylesheet" href="https://fonts.googleapis.com/css2?family=Roboto+Condensed:wght@300&display=swap">
<style>
  :root {
    --bg: #242424;
    --crimson: #8a1a13;
    --title-grey: #8c8c8c;
  }
  html, body {
    margin: 0;
    padding: 0;
    width: 1200px;
    height: 1200px;
    overflow: hidden;
    background: var(--bg);
  }
  .cover {
    position: relative;
    width: 1200px;
    height: 1200px;
    background: var(--bg);
  }
  .cover__shards {
    position: absolute;
    inset: 0;
  }
  .cover__title {
    position: absolute;
    left: 600px;
    top: 471px;
    transform: translateX(-50%);
    margin: 0;
    writing-mode: vertical-rl;
    font-family: "Roboto Condensed", "Arial Narrow", sans-serif;
    font-weight: 300;
    font-size: 27px;
    line-height: 1;
    letter-spacing: 0.02em;
    color: var(--title-grey);
    white-space: nowrap;
  }
</style>
</head>
<body>
  <main class="cover">
    <svg class="cover__shards" width="1200" height="1200" viewBox="0 0 1200 1200" aria-hidden="true">
      <defs>
        <linearGradient id="shard-fade-down" x1="0" y1="220" x2="0" y2="800" gradientUnits="userSpaceOnUse">
          <stop offset="0" stop-color="var(--crimson)" stop-opacity="0.95"/>
          <stop offset="0.45" stop-color="var(--crimson)" stop-opacity="0.7"/>
          <stop offset="1" stop-color="var(--crimson)" stop-opacity="0.05"/>
        </linearGradient>
        <linearGradient id="shard-fade-up" x1="0" y1="398" x2="0" y2="980" gradientUnits="userSpaceOnUse">
          <stop offset="0" stop-color="var(--crimson)" stop-opacity="0.05"/>
          <stop offset="0.55" stop-color="var(--crimson)" stop-opacity="0.7"/>
          <stop offset="1" stop-color="var(--crimson)" stop-opacity="0.95"/>
        </linearGradient>
      </defs>
      <polygon class="shard shard--upper" points="441,220 570,349 570,800 441,672" fill="url(#shard-fade-down)"/>
      <polygon class="shard shard--lower" points="630,398 757,528 759,980 630,851" fill="url(#shard-fade-up)"/>
    </svg>
    <h1 class="cover__title">TAVREN // SABLE HOURS</h1>
  </main>
</body>
</html>
```